Quorvane Capital Modern Business Card

We need a modern business card template designed for Quorvane Capital.
Quorvane Capital is a diversified global cryptocurrency investment fund.

The font under the logo: Hiragino Kaku Gothic Pro

Color Hexcode: Main colors white (ffffff) & teal (188383), we are open to adding #fcca46 as an accent

Target Market(s)

Accredited Investors, high net worth individuals and institutional investors

Industry/Entity Type

Investment

Contact Information for Business Card

Contact Information should contain
Name
main phone +1 720 555 0147
cell
email

Font styles to use
Sans Serif
Other font styles liked:
• Hiragino Kaku Gothic Pro

Requirements
Must have
• would like to have icons that identify the contact information
• include our website: www.quorvanecapital.example
• include our Tagline: Diversified Crypto Investment Funds
Nice to have
• Would like to have a simple back side with the logo (without the words) and plenty of space

```html
<!DOCTYPE html>
<html lang="en">
<head>
<meta charset="utf-8">
<title>Quorvane Capital – Business Card</title>
<link rel="stylesheet" href="https://fonts.googleapis.com/css2?family=Noto+Sans+JP:wght@400;500&display=swap">
<style>
  :root {
    --bg: #d4d4d4;
    --card: #ffffff;
    --teal: #188383;
    --teal-bright: #22aaa6;
    --gold: #fcca46;
    --ink: #1c1c1c;
  }
  * { box-sizing: border-box; margin: 0; padding: 0; }
  html, body { width: 1200px; height: 1200px; overflow: hidden; background: var(--bg); }
  body { position: relative; font-family: "Noto Sans JP", sans-serif; color: var(--ink); }

  .card {
    position: absolute; left: 250px; width: 700px; height: 400px;
    background: var(--card); overflow: hidden;
    box-shadow: 0 6px 18px rgba(0,0,0,.12);
  }
  .card--front { top: 130px; }
  .card--back { top: 670px; }

  .accent-band {
    position: absolute; left: 0; top: 0; bottom: 0; width: 70px;
    background: linear-gradient(180deg, #fdd65c, var(--gold));
  }

  .holder { position: absolute; left: 330px; top: 70px; }
  .holder__name { color: var(--teal-bright); font-size: 28px; font-weight: 400; letter-spacing: 1px; text-transform: uppercase; }
  .holder__role { color: var(--teal-bright); font-size: 15px; margin-top: 2px; }

  .contact-list { position: absolute; left: 330px; top: 160px; list-style: none; }
  .contact-list li { display: flex; align-items: center; gap: 12px; font-size: 17px; line-height: 28px; }
  .contact-list svg { width: 16px; height: 16px; flex: none; color: var(--teal-bright); }

  .tagline {
    position: absolute; left: 100px; bottom: 40px;
    font-size: 26px; font-weight: 400; color: var(--ink);
  }

  .brand {
    position: absolute; left: 50%; top: 50%; transform: translate(-50%, -50%);
    display: flex; align-items: center; gap: 14px;
  }
  .brand__square { width: 22px; height: 22px; background: var(--teal); }
  .brand__name { font-size: 30px; font-weight: 400; color: var(--teal); letter-spacing: 2px; text-transform: uppercase; }
</style>
</head>
<body>
  <section class="card card--front" aria-label="Business card front">
    <div class="accent-band"></div>
    <div class="holder">
      <h1 class="holder__name">Maren Holloway</h1>
      <p class="holder__role">CEO</p>
    </div>
    <ul class="contact-list">
      <li>
        <svg viewBox="0 0 16 16" aria-hidden="true"><rect x="4" y="1" width="8" height="14" rx="1.5" fill="none" stroke="currentColor" stroke-width="1.4"/><line x1="7" y1="12.5" x2="9" y2="12.5" stroke="currentColor" stroke-width="1.4"/></svg>
        +1 720 555 0193
      </li>
      <li>
        <svg viewBox="0 0 16 16" aria-hidden="true"><path d="M3 1.5l3 .5 1 3-1.8 1.3a8 8 0 0 0 4.5 4.5L11 9l3 1 .5 3-1.5 1.5C7 14 2 9 1.5 3z" fill="currentColor"/></svg>
        +1 720 555 0147
      </li>
      <li>
        <svg viewBox="0 0 16 16" aria-hidden="true"><rect x="1" y="3" width="14" height="10" fill="none" stroke="currentColor" stroke-width="1.4"/><path d="M1 3l7 6 7-6" fill="none" stroke="currentColor" stroke-width="1.4"/></svg>
        contact@quorvanecapital.example
      </li>
      <li>
        <svg viewBox="0 0 16 16" aria-hidden="true"><circle cx="8" cy="8" r="7" fill="currentColor"/><path d="M1 8h14M8 1c-3 3-3 11 0 14M8 1c3 3 3 11 0 14" fill="none" stroke="#fff" stroke-width="1"/></svg>
        www.quorvanecapital.example
      </li>
    </ul>
    <p class="tagline">Diversified Crypto Investment Funds</p>
  </section>

  <section class="card card--back" aria-label="Business card back">
    <div class="brand">
      <span class="brand__square"></span>
      <span class="brand__name">Quorvane Capital</span>
    </div>
  </section>
</body>
</html>
```